Technology Company Web Design Project

We are working with BrimLoop. They are a technology company and in need of a new website design.
BrimLoop helps companies control who (or what) can access which information inside their systems — and under what conditions. Think of them as the traffic controller for digital access and data permissions.
Instead of letting every app, employee, or AI bot freely connect to everything, GateMarrow makes sure:
• Each one only gets access to what it actually needs.
• That access follows company rules automatically.
• Those rules are enforced the same way everywhere — across apps, servers, and even AI tools.
Some competitor sites to use for inspiration:
https://www.korvanshield.com/en/lp/ac/korvanmesh.html
https://www.dunmerecharter.org
https://www.qelvo.com
Thank you for taking the time to consider designing a website for us. We are web developers based in Stockton and Los Angeles, CA, USA. Most of our projects go through the same process. Understanding this process may help you win a project with us. We custom-code all of our websites in-house. We don’t have any requirements as to what tools you use for your design, but we prefer Figma files. For any design that we label as four-stars, we send it to the client for review. The client picks the final design they want us to use. Once we complete this process, we will continue to show additional clients all the four-star sites and purchase them later. Your designs will have multiple chances to sell. For better chances of success, we ask that you follow these guidelines.
IMAGES:
If you use any images or icons in the design, we ask that you have a link to the asset so we can purchase the image/icon. Most of the designs we submit do not have the customer’s images on them unless they have some great images. Be creative; show us the feeling you are trying to portray with your image choices. Use any royalty-free site you choose. We subscribe to Tarsel and mainly use their images, but we can purchase images outside of Tarsel.
PLEASE NOTE: we will not submit designs to clients with watermarks on the images.
FONTS:
We ask that you identify the fonts used in the design. This can be done in a message if you want. We typically use Google Fonts and Tarsel Fonts.
CONTENT:
We're always open to different content and ideas. We often submit designs with stock images so the client can see our vision. We typically take pictures after the website launch to use their images with our vision. Lorem Ipsum is fine for paragraphs, but we ask that you write the headers in correct English. We want to be able to show the vision and identify the sections of the website.
INSPIRATION:
We typically add a couple of links in the brief of websites we like to help you get started in your design.
REVISIONS:
We do not often ask for revisions of the designs unless we see something in the design that may not appeal to the client. If there are slight changes that we want to make, we do that in the development process.
FEEDBACK:
We rarely give feedback on designs during the design process. We are working on many website projects and do not have the time to provide feedback. We usually respond if your request is well thought out and asks specific questions, but a note asking “feedback, please” usually goes unanswered.

```html
<!DOCTYPE html>
<html lang="en">
<head>
<meta charset="utf-8">
<title>BrimLoop — Control Access. Protect Data.</title>
<link href="https://fonts.googleapis.com/css2?family=Outfit:wght@400;500;600;700&family=Poppins:wght@400;500;600&display=swap" rel="stylesheet">
<style>
:root{
  --navy:#1f3b63;
  --navy-deep:#17304f;
  --navy-soft:#2d4d79;
  --orange:#e8822f;
  --ink:#1c2740;
  --muted:#5d6677;
  --line:#dfe3ea;
  --mist:#eef0f4;
  --white:#ffffff;
}
*{box-sizing:border-box;margin:0;padding:0}
html,body{width:1200px;height:4591px;overflow:hidden}
body{position:relative;background:var(--white);font-family:"Poppins",sans-serif;color:var(--ink)}
.abs{position:absolute}
h1,h2,h3,.display{font-family:"Outfit",sans-serif;letter-spacing:-0.02em}
.accent{color:var(--orange)}
.btn{position:absolute;z-index:3;display:flex;align-items:center;justify-content:center;border-radius:30px;font-size:11px;font-weight:600;font-family:"Poppins",sans-serif}
.btn-solid{background:var(--orange);color:#fff}
.btn-ghost{border:1.5px solid var(--navy);color:var(--navy);background:#fff}
.btn-ghost-light{border:1.5px solid #fff;color:#fff}
.center{left:0;width:1200px;text-align:center}

/* top bar */
.topbar{top:0;left:0;width:1200px;height:30px;background:var(--navy-deep);color:#fff;font-size:10px}
.topbar .notice{position:absolute;left:0;width:1200px;text-align:center;top:8px}
.topbar .util{position:absolute;right:48px;top:8px;display:flex;gap:14px}
.topbar .util span+span{border-left:1px solid rgba(255,255,255,.5);padding-left:14px}

/* hero */
.hero-bg{top:30px;left:0;width:1200px;height:720px;background:linear-gradient(#eef0f4 0%,#f6f7f9 40%,#ffffff 100%)}
.brand{display:flex;align-items:center;gap:10px;font-family:"Outfit",sans-serif;font-weight:700;color:var(--navy);letter-spacing:.06em}
.brand .dot{width:30px;height:30px;border-radius:50%;background:var(--navy)}
.nav{top:78px;left:338px;display:flex;gap:24px;font-size:11px;color:var(--ink)}
.nav .ic{width:12px;height:12px;border:1.6px solid var(--ink);border-radius:50%;margin-top:2px}
.hero-title{top:166px;font-size:48px;font-weight:600;line-height:50px;color:var(--navy);z-index:3}
.hero-sub{top:284px;font-size:12px;line-height:22px;color:var(--muted);z-index:3}
.hero-art{top:400px;left:98px;width:1002px;height:336px;border-radius:6px;background:radial-gradient(ellipse at 30% 45%,#3a5a88 0%,#dde4ee 55%,#f6f7f9 80%);z-index:1}

/* client names */
.clients{top:806px;left:104px;width:992px;display:flex;justify-content:space-between;align-items:center}
.client{display:flex;align-items:center;gap:7px;font-family:"Outfit",sans-serif;font-size:22px;font-weight:500;color:#3b4558}
.client i{display:block;width:14px;height:14px;background:#3b4558}
.client i.r{border-radius:50%}

/* arc backgrounds */
.arc{left:-300px;width:1800px;border-radius:50% 50% 0 0/240px 240px 0 0;background:linear-gradient(#eceef2,#ffffff 60%)}

/* traffic section */
.sec-title{font-size:29px;font-weight:600;color:var(--navy);line-height:34px}
.sec-sub{font-size:11.5px;line-height:19px;color:var(--muted)}
.feature{left:160px;width:357px;display:flex;gap:22px}
.feature svg{flex:none}
.feature h3{font-size:17px;font-weight:500;color:var(--navy);margin-bottom:6px;letter-spacing:0}
.feature p{font-size:11px;line-height:18px;color:var(--muted)}
.divider{left:240px;width:277px;height:1px;background:var(--line)}

.shot-card{top:1163px;left:578px;width:451px;height:481px;border:3px solid #dfe2e8;border-radius:24px;background:#fff}
.shot{top:1202px;left:622px;width:360px;height:381px;border-radius:12px;background:var(--navy);overflow:hidden;font-size:6.5px;color:#cfd8e6}
.shot .bar{height:22px;background:#16294a;display:flex;align-items:center;gap:5px;padding-left:10px}
.shot .bar b{width:7px;height:7px;border-radius:50%;background:#e2675c}
.shot .bar b:nth-child(2){background:#e8b43f}
.shot .bar b:nth-child(3){background:#5cc06a}
.shot .url{position:absolute;top:27px;left:40px;width:300px;height:12px;border-radius:6px;background:#2c4870;padding:2px 8px}
.shot .rail{position:absolute;top:46px;left:0;width:26px;height:335px;background:#1a3154}
.shot .pane{position:absolute;left:38px;width:310px;border-radius:6px;background:#2a4770;padding:6px 9px}
.shot .chip{display:inline-block;background:#3d5c88;border-radius:3px;padding:1px 4px;margin-left:4px}
.shot .ok{display:inline-block;width:11px;height:11px;border-radius:50%;background:#5cc06a;vertical-align:middle;margin-right:4px}
.caption{top:1607px;left:578px;width:451px;text-align:center;font-size:10px;color:var(--ink)}

/* product cards */
.pcard{top:1883px;width:252px;height:274px;border-radius:18px;background:#fff;box-shadow:0 14px 40px rgba(31,59,99,.10);text-align:center;padding-top:38px}
.pcard h3{font-size:17px;font-weight:500;color:var(--navy);margin-top:18px;letter-spacing:0}
.pcard p{font-size:11px;line-height:18px;color:var(--muted);margin:10px 30px 0}

/* trust band */
.band{top:2255px;left:105px;width:990px;height:544px;border-radius:60px;background:linear-gradient(120deg,#1d385f 0%,#2b4a75 55%,#1d385f 100%);overflow:hidden}
.pill{height:104px;border-radius:60px;background:rgba(255,255,255,.09);display:flex;align-items:center;gap:20px;color:#fff}
.pill h3{font-size:15px;font-weight:500;letter-spacing:0}
.pill p{font-size:10.5px;line-height:16px;color:#c9d3e2;margin-top:4px}
.pill .icon{flex:none;width:64px;height:64px;border-radius:50%;background:rgba(255,255,255,.06);display:flex;align-items:center;justify-content:center}
.band-title{top:2428px;left:705px;font-size:29px;font-weight:600;line-height:36px;color:#fff}
.band-sub{top:2516px;left:705px;width:290px;font-size:11px;line-height:19px;color:#d7dfea}

/* industries */
.ind{top:3070px;height:339px;border-radius:22px;overflow:hidden}
.ind span{position:absolute;left:28px;bottom:30px;font-family:"Outfit",sans-serif;font-weight:600;font-size:28px;color:#fff}

/* resources */
.rcard{top:3609px;width:252px;height:183px;border-radius:16px;background:#fff;border:1px solid #eceef2;box-shadow:0 14px 34px rgba(31,59,99,.08);padding:34px 32px}
.rcard h3{font-size:17px;font-weight:500;color:var(--navy);letter-spacing:0}
.rcard p{font-size:11px;line-height:19px;color:var(--muted);margin-top:12px}
.rcard a{position:absolute;left:0;width:100%;bottom:28px;text-align:center;font-size:10.5px;font-weight:600;color:var(--orange);text-decoration:none}

/* cta */
.cta{top:3905px;left:105px;width:990px;height:249px;border-radius:60px;background:linear-gradient(110deg,#1c365d,#2c4b77);overflow:hidden}
.cta h2{position:absolute;left:73px;top:141px;font-size:28px;font-weight:600;color:#fff}
.cta p{position:absolute;left:73px;top:185px;font-size:11px;font-weight:600;color:#fff}

/* footer */
.foot-arc{top:4180px}
.fcol{top:4270px;font-size:11px;color:var(--muted)}
.fcol h4{font-family:"Outfit",sans-serif;font-size:16px;font-weight:600;color:var(--navy);margin-bottom:18px}
.fcol li{list-style:none;line-height:22.5px}
.foot-line{top:4493px;left:105px;width:990px;height:1px;background:var(--line)}
.social{top:4528px;left:148px;display:flex;gap:10px}
.social i{display:block;width:28px;height:28px;border-radius:50%;border:1.5px solid var(--navy)}
.legal{top:4536px;font-size:10.5px;color:var(--ink)}
.chat{top:4466px;left:1122px;width:46px;height:46px;border-radius:50% 50% 50% 8px;background:var(--orange)}
</style>
</head>
<body>

<div class="abs topbar">
  <div class="notice">Important Update: See the DCR Blog for more details.</div>
  <div class="util"><span>Partners</span><span>Sign In</span></div>
</div>

<div class="abs hero-bg"></div>
<div class="abs brand" style="top:70px;left:106px;font-size:22px"><span class="dot"></span>BRIMLOOP</div>
<nav class="abs nav">
  <span>Platform ⌄</span><span>Solutions ⌄</span><span>Resources ⌄</span><span>Developers ⌄</span><span>Support</span>
  <span class="ic"></span><span class="ic"></span>
</nav>
<div class="btn btn-solid" style="top:67px;left:859px;width:114px;height:40px">Talk to Sales</div>
<div class="btn btn-ghost" style="top:67px;left:981px;width:113px;height:40px;border-color:#7a8496">Try BrimLoop</div>

<h1 class="abs center hero-title">Control Access. <span class="accent">Protect Data.</span><br>Simplify Compliance.</h1>
<p class="abs center hero-sub">BrimLoop helps organizations manage who (or what) can access which data and under what conditions.<br>Your digital world, securely connected and automatically enforced.</p>
<div class="abs hero-art" role="img" aria-label="Large navy wing illustration beside an outlined wing with connected network nodes"></div>
<div class="btn btn-solid" style="top:350px;left:460px;width:134px;height:38px">Request a Demo</div>
<div class="btn btn-ghost" style="top:350px;left:604px;width:136px;height:38px">How it Works</div>

<div class="abs clients">
  <div class="client">Corvalt</div>
  <div class="client"><i class="r"></i>Mirenza</div>
  <div class="client" style="font-size:18px">Tandrel</div>
  <div class="client"><i></i>Plumtide</div>
  <div class="client" style="font-weight:700">Harrowick</div>
  <div class="client" style="font-size:18px"><i class="r"></i>Voyalin</div>
</div>

<div class="abs arc" style="top:910px;height:900px"></div>
<h2 class="abs center sec-title" style="top:1026px">The Traffic <span class="accent">Controller</span> for Digital Access</h2>
<p class="abs center sec-sub" style="top:1076px">Instead of letting every app, employee, or AI bot freely connect to everything, GateMarrow’s ensures<br>access is always intentional, rule-based, and monitored.</p>

<div class="abs feature" style="top:1228px">
  <svg width="56" height="56" viewBox="0 0 56 56" fill="none" stroke="#1f3b63" stroke-width="1.6"><circle cx="28" cy="28" r="20"/><circle cx="28" cy="28" r="12"/><circle cx="28" cy="28" r="4" stroke="#e8822f"/><path d="M28 2v12M28 42v12M2 28h12M42 28h12"/></svg>
  <div><h3>Precision Access</h3><p>Give every user, system, and AI tool exactly the access they need — nothing more.</p></div>
</div>
<div class="abs divider" style="top:1318px"></div>
<div class="abs feature" style="top:1344px">
  <svg width="56" height="56" viewBox="0 0 56 56" fill="none" stroke="#1f3b63" stroke-width="1.6"><rect x="3" y="8" width="50" height="40" rx="3"/><path d="M3 17h50"/><circle cx="20" cy="33" r="7" stroke="#e8822f"/><circle cx="36" cy="33" r="7"/></svg>
  <div><h3>Policy Automation</h3><p>Access policies apply automatically across apps, APIs, and clouds.</p></div>
</div>
<div class="abs divider" style="top:1434px"></div>
<div class="abs feature" style="top:1460px">
  <svg width="56" height="56" viewBox="0 0 56 56" fill="none" stroke="#1f3b63" stroke-width="1.6"><path d="M28 3l21 8v15c0 14-9 23-21 27C16 49 7 40 7 26V11z"/><path d="M28 12l13 5v9c0 9-6 15-13 18-7-3-13-9-13-18v-9z"/><path d="M28 20l2.6 5.4 5.9.8-4.3 4.1 1 5.9L28 33.4l-5.2 2.8 1-5.9-4.3-4.1 5.9-.8z" stroke="#e8822f"/></svg>
  <div><h3>Universal Enforcement</h3><p>Rules enforced consistently — across servers, SaaS tools, and internal systems.</p></div>
</div>
<div class="btn btn-solid" style="top:1576px;left:160px;width:138px;height:38px">Request a Demo</div>

<div class="abs shot-card"></div>
<div class="abs shot">
  <div class="bar"><b></b><b></b><b></b><span style="margin-left:10px">Policy Hub</span></div>
  <div class="url">app.qelvo.com/systems/policy-builder</div>
  <div class="rail"></div>
  <div class="pane" style="top:50px;background:transparent;padding:0">Systems / Policy Builder</div>
  <div class="pane" style="top:64px;height:60px">Validation<br><br><span class="ok"></span>Policy Tests <span style="margin-left:70px" class="chip">100%</span> Decision Impact</div>
  <div class="pane" style="top:132px;height:40px">Decision&nbsp;&nbsp; Priority <span class="chip">Deny overrides Allow</span>&nbsp;&nbsp; Default decision <span class="chip">Deny</span> <span class="chip" style="float:right">Evaluate</span></div>
  <div class="pane" style="top:180px;height:110px;line-height:20px">Allow<br>input&nbsp; account.product_code <span class="chip">equals</span> <span class="chip">direct-deposit</span><br>and&nbsp; input&nbsp; account.status <span class="chip">equals</span> <span class="chip">open</span><br>and&nbsp; to Account Owner</div>
  <div class="pane" style="top:302px;width:60px;padding:3px 8px">+ Create rule</div>
</div>
<p class="abs caption">Interested to see more? Checkout the <span class="accent">Maintainer Track Session</span> from Kelvrin Summit.</p>

<h2 class="abs center sec-title" style="top:1734px">Meet GateMarrow — <span class="accent">Intelligent</span> Access<br>Control for Modern Enterprises</h2>
<p class="abs center sec-sub" style="top:1817px">A unified platform that defines, enforces, and audits access across your entire digital ecosystem.</p>

<div class="abs pcard" style="left:205px">
  <svg width="60" height="76" viewBox="0 0 60 76" fill="none" stroke="#1f3b63" stroke-width="1.6"><circle cx="30" cy="28" r="22"/><circle cx="30" cy="28" r="12" stroke="#e8822f"/><circle cx="30" cy="28" r="4"/><path d="M22 50v10h16V50M24 66h12M26 71h8"/></svg>
  <h3>BrimLoop Define</h3><p>Build access rules in plain language that match company policies.</p>
</div>
<div class="abs pcard" style="left:474px">
  <svg width="66" height="76" viewBox="0 0 66 76" fill="none" stroke="#1f3b63" stroke-width="1.6"><rect x="6" y="8" width="40" height="58" rx="3"/><rect x="17" y="3" width="18" height="9" rx="2"/><path d="M13 24l3 3 5-6M26 24h13M13 36l3 3 5-6M26 36h13M13 48l3 3 5-6M26 48h10"/><path d="M44 50l14 14M40 54l8-8" stroke="#e8822f"/><path d="M38 70h22"/></svg>
  <h3>BrimLoop Enforce</h3><p>Apply them automatically everywhere — cloud, on-prem, or hybrid.</p>
</div>
<div class="abs pcard" style="left:744px">
  <svg width="66" height="76" viewBox="0 0 66 76" fill="none" stroke="#1f3b63" stroke-width="1.6"><path d="M6 4h30l10 10v56H6z"/><path d="M14 50V34M22 50V24M30 50V30M38 50V38"/><circle cx="44" cy="54" r="11" stroke="#e8822f"/><path d="M39 54l4 4 6-7M52 62l9 9" stroke="#e8822f"/></svg>
  <h3>BrimLoop Audit</h3><p>Monitor and prove compliance anytime with built-in analytics.</p>
</div>

<div class="abs band"></div>
<div class="abs pill" style="top:2318px;left:216px;width:380px;padding-left:18px">
  <span class="icon"><svg width="38" height="38" viewBox="0 0 38 38" fill="none" stroke="#e8822f" stroke-width="1.5"><circle cx="19" cy="19" r="15"/><rect x="12" y="17" width="14" height="11" rx="2"/><path d="M15 17v-4a4 4 0 018 0v4"/></svg></span>
  <div><h3>Zero Trust, Simplified</h3><p>Built around Zero Trust principles,<br>without the complexity.</p></div>
</div>
<div class="abs pill" style="top:2425px;left:250px;width:376px;justify-content:flex-end;text-align:right;padding-right:18px">
  <div><h3>Cross-Platform</h3><p>Works across Nimbra, Veltcloud, Orrin<br>Cloud, and on-prem systems.</p></div>
  <span class="icon"><svg width="38" height="38" viewBox="0 0 38 38" fill="none" stroke="#e8822f" stroke-width="1.5"><rect x="4" y="8" width="24" height="17" rx="2"/><path d="M10 30h12M16 25v5"/><rect x="24" y="14" width="10" height="18" rx="2"/></svg></span>
</div>
<div class="abs pill" style="top:2531px;left:216px;width:380px;padding-left:18px">
  <span class="icon"><svg width="38" height="38" viewBox="0 0 38 38" fill="none" stroke="#e8822f" stroke-width="1.5"><circle cx="19" cy="19" r="9"/><circle cx="19" cy="19" r="3"/><path d="M19 3v7M19 28v7M3 19h7M28 19h7M8 8l5 5M25 25l5 5M30 8l-5 5M13 25l-5 5"/></svg></span>
  <div><h3>Built for AI &amp; Automation</h3><p>Control what your AI agents<br>can see or do.</p></div>
</div>
<div class="abs pill" style="top:2637px;left:250px;width:376px;justify-content:flex-end;text-align:right;padding-right:18px">
  <div><h3>Compliance Ready</h3><p>Automatically meet SOC2, ISO, and<br>GDPR standards.</p></div>
  <span class="icon"><svg width="38" height="38" viewBox="0 0 38 38" fill="none" stroke="#e8822f" stroke-width="1.5"><rect x="7" y="4" width="22" height="30" rx="2"/><path d="M12 12h12M12 18h12M12 24h8"/><circle cx="28" cy="28" r="6"/></svg></span>
</div>
<h2 class="abs band-title">Why <span class="accent">Leading</span> Teams<br>Trust BrimLoop</h2>
<p class="abs band-sub">Because secure access shouldn’t slow your business — it should enable it.</p>
<div class="btn btn-solid" style="top:2576px;left:705px;width:218px;height:38px">See Customer Success Stories</div>

<div class="abs arc" style="top:2840px;height:600px"></div>
<h2 class="abs center sec-title" style="top:2936px">Built for Every <span class="accent">Industry</span><br>that Values Security</h2>
<p class="abs center sec-sub" style="top:3015px">From finance to healthcare, BrimLoop adapts to your unique compliance and access needs.</p>
<div class="abs ind" style="left:105px;width:237px;background:linear-gradient(160deg,#4a3a2a,#a87a42 55%,#2a2620)" role="img" aria-label="Hand stacking coins in front of a glowing market chart"><span>Finance</span></div>
<div class="abs ind" style="left:355px;width:239px;background:linear-gradient(160deg,#3b5878,#1f3b63 60%,#0f2036)" role="img" aria-label="Clinician holding a glowing digital health interface"><span>Healthcare</span></div>
<div class="abs ind" style="left:606px;width:239px;background:linear-gradient(160deg,#6b8aa8,#2d4b6d 55%,#14283f)" role="img" aria-label="Engineer working with holographic technology screens"><span>Technology</span></div>
<div class="abs ind" style="left:858px;width:237px;background:linear-gradient(160deg,#5a7896,#2a4565 55%,#142840)" role="img" aria-label="Government building with digital security overlay"><span>Government</span></div>

<h2 class="abs center sec-title" style="top:3517px">Learn. <span class="accent">Explore</span>. Evolve.</h2>
<p class="abs center sec-sub" style="top:3562px">Stay ahead with BrimLoop insights and whitepapers.</p>
<div class="abs rcard" style="left:205px"><h3>Whitepaper</h3><p>The Future of Zero Trust<br>Access</p><a>Request a Demo</a></div>
<div class="abs rcard" style="left:474px"><h3>Blog</h3><p>Managing AI Access in Hybrid<br>Work Environments</p><a>View all Blog</a></div>
<div class="abs rcard" style="left:744px"><h3>Guide</h3><p>Building Scalable Access<br>Policies for Multi-Cloud</p><a>Download Guide</a></div>

<div class="abs cta">
  <h2>Ready to Take <span class="accent">Control</span> of Access?</h2>
  <p>Schedule a personalized demo and see how BrimLoop transforms your security posture.</p>
</div>
<div class="btn btn-solid" style="top:4012px;left:745px;width:136px;height:38px">Request a Demo</div>
<div class="btn btn-ghost-light" style="top:4012px;left:888px;width:135px;height:38px">Talk to a Specialist</div>

<div class="abs arc foot-arc" style="height:420px"></div>
<div class="abs brand" style="top:4330px;left:156px;font-size:34px"><span class="dot" style="width:40px;height:40px"></span>BRIMLOOP</div>
<div class="abs fcol" style="left:419px"><h4>Company</h4><ul><li>About Us</li><li>Leadership Team</li><li>Careers</li><li>Trust Center</li><li>Korvan Newsroom</li></ul></div>
<div class="abs fcol" style="left:578px"><h4>Why BrimLoop</h4><ul><li>Customer Stories</li><li>Solutions</li><li>Industries</li><li>Analyst Reports</li></ul></div>
<div class="abs fcol" style="left:735px"><h4>Get Started</h4><ul><li>Talk with a Strategist</li><li>Try Korvan</li><li>Product Demos</li></ul></div>
<div class="abs fcol" style="left:906px"><h4>Support</h4><ul><li>Support Portal</li><li>Community Forum</li><li>Documentation</li><li>Frequently Asked Questions</li></ul></div>
<div class="abs chat" role="img" aria-label="Live chat"></div>
<div class="abs foot-line"></div>
<div class="abs social" aria-label="Social profiles"><i></i><i></i><i></i><i></i><i></i><i></i></div>
<div class="abs legal" style="left:486px">© Copyright 2025 BrimLoop. All rights reserved.</div>
<div class="abs legal" style="left:808px;display:flex;gap:22px"><span>Legal</span><span>Privacy</span><span>Security</span><span>Cookie Settings</span></div>

</body>
</html>
```